Designing a front label called Perla Luna / Bottle Label for a Sparkling Wine called Luna Perla

We want to bring a Luna Perla on the market. For this we need a front label. Bottle is painted white and the capsule is fixed. (Black with golden lettering K.Wendrich) Height of label max. 8.5cm. The whole thing should be fresh teen. Happy with reference to Ice .... etc. Secco is the German version of Prosecco. But better. There are currently many Luna Perla on the market. We also want one now. www.wendrich-kellerei.de We have a nice white lacquered TRV bottle with capsule. it just fehtl the right label. Sender K.Wendrich does not have to be on top ... but if it fits. Lettering is already in the capsule anyway.

Target Market(s)

Supermarket, gals, party, alcohol, RRP 4.99 €

Font styles to use
Decorative

Colors

Designer to choose colors to be used in the design.

Requirements
Must have
• Self-adhesive label, printable data in 4c, reference to ice, black, golden reference to the capsule.
Nice to have
• Ice cubes, cool, cool.
Should not have
• boredom

```html
<!DOCTYPE html>
<html lang="de">
<head>
<meta charset="utf-8">
<title>Luna Perla – Front Label</title>
<link rel="stylesheet" href="https://fonts.googleapis.com/css2?family=Parisienne&family=Playfair+Display:wght@500&family=Marcellus&display=swap">
<style>
  :root {
    --backdrop: #333333;
    --label-black: #000000;
    --gold: #d9a84a;
    --gold-light: #f2d27a;
    --gold-deep: #9c7226;
    --foil-light: #ead6a4;
    --foil-mid: #d4b574;
    --foil-deep: #b8944f;
    --ice: #e9f3f6;
    --ice-edge: #bcd6de;
    --ink: #0b0906;
  }
  html, body {
    margin: 0;
    padding: 0;
    width: 1200px;
    height: 1200px;
    overflow: hidden;
    background: var(--backdrop);
  }
  .canvas {
    position: relative;
    width: 1200px;
    height: 1200px;
    background: var(--backdrop);
  }
  .label {
    position: absolute;
    left: 170px;
    top: 25px;
    width: 860px;
    height: 1150px;
    background: var(--label-black);
    overflow: hidden;
  }
  .rule {
    position: absolute;
    background: var(--gold);
  }
  .rule--top { left: 270px; top: 30px; width: 320px; height: 2px; }
  .rule--bottom { left: 270px; top: 1117px; width: 320px; height: 2px; }
  .rule--left { left: 36px; top: 285px; width: 3px; height: 577px; }
  .rule--right { left: 821px; top: 285px; width: 3px; height: 577px; }

  .corner-ornament {
    position: absolute;
    width: 230px;
    height: 250px;
  }
  .corner-ornament--tl { left: 0; top: 0; background: radial-gradient(ellipse at 6% 6%, rgba(217,168,74,0.55) 0%, rgba(156,114,38,0.25) 35%, transparent 68%); }
  .corner-ornament--tr { right: 0; top: 0; background: radial-gradient(ellipse at 94% 6%, rgba(217,168,74,0.55) 0%, rgba(156,114,38,0.25) 35%, transparent 68%); }
  .corner-ornament--bl { left: 0; bottom: 0; background: radial-gradient(ellipse at 6% 94%, rgba(217,168,74,0.55) 0%, rgba(156,114,38,0.25) 35%, transparent 68%); }
  .corner-ornament--br { right: 0; bottom: 0; background: radial-gradient(ellipse at 94% 94%, rgba(217,168,74,0.55) 0%, rgba(156,114,38,0.25) 35%, transparent 68%); }

  .house-mark {
    position: absolute;
    left: 0;
    top: 150px;
    width: 860px;
    display: flex;
    align-items: center;
    justify-content: center;
    gap: 12px;
  }
  .house-mark__ring {
    width: 14px;
    height: 14px;
    border-radius: 50%;
    border: 2px solid var(--gold);
  }
  .house-mark__name {
    font-family: "Marcellus", serif;
    font-size: 22px;
    letter-spacing: 6px;
    text-transform: uppercase;
    color: var(--gold);
    line-height: 1;
  }

  .producer {
    position: absolute;
    left: 0;
    top: 312px;
    width: 860px;
    margin: 0;
    text-align: center;
    font-family: "Parisienne", cursive;
    font-size: 66px;
    line-height: 1;
    color: var(--gold);
  }

  .divider {
    position: absolute;
    left: 258px;
    width: 344px;
    height: 8px;
  }
  .divider::before, .divider::after {
    content: "";
    position: absolute;
    top: 3px;
    width: 150px;
    height: 1px;
    background: var(--gold-deep);
  }
  .divider::before { left: 0; }
  .divider::after { right: 0; }
  .divider__dot {
    position: absolute;
    left: 168px;
    top: 0;
    width: 7px;
    height: 7px;
    border-radius: 50%;
    background: var(--gold);
  }
  .divider--upper { top: 403px; }
  .divider--lower { top: 967px; }

  .foil-stroke {
    position: absolute;
    left: 150px;
    top: 455px;
    width: 565px;
    height: 490px;
  }

  .ice-cubes {
    position: absolute;
    left: 0;
    top: 0;
    width: 860px;
    height: 1150px;
    pointer-events: none;
  }

  .product-name {
    position: absolute;
    left: 0;
    top: 528px;
    width: 860px;
    margin: 0;
    text-align: center;
    font-family: "Playfair Display", serif;
    font-weight: 500;
    color: var(--ink);
    font-size: 142px;
    line-height: 158px;
  }

  .net-content {
    position: absolute;
    left: 0;
    top: 1003px;
    width: 860px;
    margin: 0;
    text-align: center;
    font-family: "Marcellus", serif;
    font-size: 38px;
    color: var(--gold);
  }
</style>
</head>
<body>
<main class="canvas">
  <section class="label">
    <div class="corner-ornament corner-ornament--tl" role="img" aria-label="Gold baroque scroll ornament, top left corner"></div>
    <div class="corner-ornament corner-ornament--tr" role="img" aria-label="Gold baroque scroll ornament, top right corner"></div>
    <div class="corner-ornament corner-ornament--bl" role="img" aria-label="Gold baroque scroll ornament, bottom left corner"></div>
    <div class="corner-ornament corner-ornament--br" role="img" aria-label="Gold baroque scroll ornament, bottom right corner"></div>

    <div class="rule rule--top"></div>
    <div class="rule rule--bottom"></div>
    <div class="rule rule--left"></div>
    <div class="rule rule--right"></div>

    <div class="house-mark">
      <span class="house-mark__ring"></span>
      <span class="house-mark__name">K.Wendrich</span>
    </div>

    <p class="producer">K.Wendrich</p>
    <div class="divider divider--upper"><span class="divider__dot"></span></div>

    <svg class="foil-stroke" viewBox="0 0 565 490" role="img" aria-label="Textured gold foil brush stroke with a frosty edge">
      <defs>
        <linearGradient id="foil" x1="0" y1="0" x2="1" y2="1">
          <stop offset="0" stop-color="var(--foil-light)"/>
          <stop offset="0.55" stop-color="var(--foil-mid)"/>
          <stop offset="1" stop-color="var(--foil-deep)"/>
        </linearGradient>
        <linearGradient id="frost" x1="0" y1="0" x2="0" y2="1">
          <stop offset="0" stop-color="var(--ice)" stop-opacity="0.55"/>
          <stop offset="0.35" stop-color="var(--ice)" stop-opacity="0"/>
        </linearGradient>
      </defs>
      <path fill="url(#foil)" d="M120 72 L210 55 L300 40 L380 30 L470 20 L515 45 L500 70 L530 85 L545 140 L520 160 L552 190 L540 240 L520 250 L555 300 L535 330 L520 360 L500 400 L470 430 L380 445 L300 462 L200 478 L120 485 L140 455 L90 440 L60 420 L30 380 L20 330 L40 300 L15 260 L10 200 L40 170 L55 120 L90 100 Z"/>
      <path fill="url(#frost)" d="M120 72 L210 55 L300 40 L380 30 L470 20 L515 45 L500 70 L530 85 L545 140 L520 160 L552 190 L540 240 L520 250 L555 300 L535 330 L520 360 L500 400 L470 430 L380 445 L300 462 L200 478 L120 485 L140 455 L90 440 L60 420 L30 380 L20 330 L40 300 L15 260 L10 200 L40 170 L55 120 L90 100 Z"/>
    </svg>

    <svg class="ice-cubes" viewBox="0 0 860 1150" aria-hidden="true">
      <g fill="none" stroke="var(--ice-edge)" stroke-width="2" stroke-linejoin="round">
        <rect x="96" y="470" width="38" height="38" rx="7" transform="rotate(-14 115 489)"/>
        <rect x="112" y="520" width="24" height="24" rx="5" transform="rotate(18 124 532)"/>
        <rect x="724" y="880" width="40" height="40" rx="7" transform="rotate(12 744 900)"/>
        <rect x="704" y="936" width="24" height="24" rx="5" transform="rotate(-20 716 948)"/>
      </g>
      <g fill="var(--ice)">
        <circle cx="107" cy="482" r="3"/>
        <circle cx="736" cy="892" r="3"/>
      </g>
    </svg>

    <h1 class="product-name">Luna<br>Perla</h1>

    <div class="divider divider--lower"><span class="divider__dot"></span></div>
    <p class="net-content">Net wt.1fl oz</p>
  </section>
</main>
</body>
</html>
```